Website design for KORVEL – data platform for healthcare & social housing

We’re looking for a clean, modern multi-page website design for KORVEL — a data platform for healthcare and social housing.

📎 Please read the attached PDF for full structure, context, and design guidance.
The briefing is essential to understanding this project.

➡️ For the initial submission, only the homepage design (including header and footer) is required.

This will help us assess design direction and fit.

The full project includes four levels (homepage, general page, product overview, and product detail), which will be completed after selecting the final designer.

Industry/Entity Type

data platform for healthcare & social housing

Number of Pages Required

1 page

Font styles to use
Sans Serif

Requirements
Must have
• Please read the attached PDF
Nice to have
Should not have

```html
<!DOCTYPE html>
<html lang="en">
<head>
<meta charset="utf-8">
<title>KORVEL – Data platform for healthcare & social housing</title>
<link href="https://fonts.googleapis.com/css2?family=Lato:wght@400;700&family=Michroma&display=swap" rel="stylesheet">
<style>
:root{
  --navy:#12407e;
  --navy-dark:#0c2f60;
  --orange:#f47c0c;
  --blue:#2d7fd3;
  --ink:#1d1d1f;
  --muted:#555b66;
  --line:#cfd3d9;
  --footer:#f3f4f6;
  --white:#ffffff;
}
*{margin:0;padding:0;box-sizing:border-box}
html,body{width:1200px;height:4301px;overflow:hidden;background:var(--white)}
body{position:relative;font-family:'Lato',sans-serif;color:var(--ink)}
.abs{position:absolute}
.display{font-family:'Michroma',sans-serif;text-transform:uppercase;letter-spacing:4px;color:var(--ink)}
.btn{position:absolute;display:flex;align-items:center;justify-content:center;background:var(--orange);color:var(--white);font-size:14px;font-weight:700;border-radius:8px}
.placeholder{position:absolute}

/* header */
.site-header{position:absolute;left:0;top:0;width:1200px;height:88px;background:var(--white);z-index:3}
.brand{position:absolute;left:60px;top:24px;display:flex;align-items:center;gap:10px;font-size:34px;font-weight:700;color:var(--navy);letter-spacing:6px}
.brand-mark{width:14px;height:14px;background:var(--orange)}
.nav a{position:absolute;top:41px;font-size:14px;color:var(--ink);text-decoration:none}

/* hero */
.hero-title{position:absolute;left:0;width:1200px;text-align:center;color:var(--white)}
.hero-card{position:absolute;left:60px;top:536px;width:217px;height:108px;border:1px solid rgba(255,255,255,.7);border-radius:10px;background:rgba(255,255,255,.18)}
.hero-card .thumb{position:absolute;left:12px;top:14px;width:68px;height:80px;border-radius:4px;background:linear-gradient(135deg,#5d7ea8,#cfd9e6)}
.hero-card .stat{position:absolute;left:92px;top:18px;color:var(--white);font-size:17px;font-weight:700}
.hero-card .label{position:absolute;left:92px;top:46px;color:var(--white);font-size:10px}
.hero-card .small{position:absolute;left:92px;top:64px;width:112px;color:rgba(255,255,255,.85);font-size:7px;line-height:1.3}

/* benefits */
.section-title{position:absolute;font-size:22px}
.benefit{position:absolute;width:240px;text-align:center}
.benefit .num{margin:0 auto;width:72px;height:72px;border:1px solid #f6c79a;border-radius:8px;display:flex;align-items:center;justify-content:center;font-size:30px;color:var(--ink);box-shadow:0 4px 10px rgba(244,124,12,.12)}
.benefit h3{margin-top:32px;font-size:17px;font-weight:400}
.benefit p{margin-top:22px;font-size:11px;line-height:1.8;color:var(--muted)}

/* about */
.body-copy{font-size:11px;line-height:1.8;color:var(--muted)}
.stat-big{position:absolute;width:140px;text-align:center;left:57px}
.stat-big strong{display:block;font-size:32px;font-weight:400;color:var(--orange)}
.stat-big span{display:block;font-size:21px;line-height:1.1}

/* timeline */
.step{position:absolute;top:2370px;width:40px;text-align:center;font-size:16px;margin-left:-20px}
.step-dot{position:absolute;top:2406px;width:12px;height:12px;border-radius:50%;background:var(--orange);margin-left:-6px}

/* accordion */
.acc-row{position:absolute;left:60px;width:1080px;height:75px;border-top:2px solid #d8d8d8}
.acc-row .idx{position:absolute;left:13px;top:29px;font-size:16px;color:var(--muted)}
.acc-row .name{position:absolute;left:74px;top:29px;font-size:17px;color:var(--muted)}
.acc-row .icon{position:absolute;left:1032px;top:29px;width:22px;height:22px;border-radius:50%;background:var(--orange)}
.acc-row.open .name{color:var(--ink);font-weight:700}
.acc-row.open .icon{background:var(--navy)}

.metric-card{position:absolute;left:125px;top:2969px;width:314px;height:297px;border:1px solid rgba(255,255,255,.25);border-radius:12px;background:rgba(255,255,255,.08)}
.metric-card .val{position:absolute;left:42px;font-size:32px;color:var(--orange)}
.metric-card .val small{font-size:15px}
.metric-card p{position:absolute;left:42px;font-size:11px;line-height:2;color:var(--white)}

/* testimonials */
.avatar{position:absolute;border-radius:50%;background:linear-gradient(135deg,#9aa3ad,#d8dde2)}

/* footer */
.site-footer{position:absolute;left:0;top:3881px;width:1200px;height:420px;background:var(--footer)}
.foot-col h4{position:absolute;font-size:17px;font-weight:400}
.foot-link{position:absolute;font-size:14px;color:var(--ink)}
.foot-dot{display:inline-block;width:18px;height:18px;border-radius:50%;background:var(--navy);vertical-align:middle;margin-right:10px}
.foot-divider{position:absolute;top:66px;width:1px;height:192px;background:#cfcfcf}
</style>
</head>
<body>

<header class="site-header">
  <div class="brand"><span class="brand-mark"></span>KORVEL</div>
  <nav class="nav">
    <a style="left:402px">Home</a>
    <a style="left:487px">About Us</a>
    <a style="left:595px">Platform</a>
    <a style="left:695px">Solutions</a>
    <a style="left:803px">Resources</a>
  </nav>
  <div class="btn" style="left:983px;top:25px;width:132px;height:48px;font-weight:400">Contact Us</div>
</header>

<!-- hero -->
<section class="hero">
  <svg class="abs" style="left:0;top:88px" width="1200" height="800" aria-hidden="true">
    <defs>
      <linearGradient id="heroBlue" x1="0" y1="0" x2="1" y2="1">
        <stop offset="0" stop-color="#6fb0ea"/>
        <stop offset=".5" stop-color="#2f7ed1"/>
        <stop offset="1" stop-color="#1f5fb0"/>
      </linearGradient>
      <linearGradient id="heroFade" x1="0" y1="0" x2="0" y2="1">
        <stop offset="0" stop-color="#ffffff"/>
        <stop offset="1" stop-color="#fdf2ea"/>
      </linearGradient>
    </defs>
    <rect width="1200" height="800" fill="url(#heroFade)"/>
    <path d="M0 0H1200V480Q600 330 0 560Z" fill="url(#heroBlue)"/>
  </svg>
  <div class="placeholder" role="img" aria-label="Background photo of healthcare workers and molecular strands" style="left:850px;top:120px;width:350px;height:420px;background:linear-gradient(160deg,rgba(255,255,255,0),rgba(220,235,250,.25))"></div>
  <h1 class="hero-title display" style="top:150px;font-size:48px;letter-spacing:8px">More Impact</h1>
  <p class="hero-title display" style="top:228px;font-size:20px;letter-spacing:5px">With better control over data</p>
  <div class="placeholder" role="img" aria-label="Laptop showing the KORVEL dashboard with revenue, clients and to-do list" style="left:205px;top:309px;width:793px;height:551px;border-radius:16px 16px 40px 40px;background:linear-gradient(180deg,#1a1d22 0,#1a1d22 4%,#eef1f7 6%,#f6f8fb 70%,#b9bcc2 86%,#8e9197 100%)"></div>
  <div class="hero-card">
    <div class="thumb" role="img" aria-label="Photo of a hand on a tablet"></div>
    <div class="stat">76,285K+</div>
    <div class="label">Experience the Future</div>
    <div class="small">Explore the high tech, low life world where the</div>
  </div>
</section>

<!-- key benefits -->
<section>
  <h2 class="section-title display" style="left:0;width:1200px;text-align:center;top:943px">Key Benefits</h2>
  <div class="benefit" style="left:69px;top:1013px"><div class="num">01</div><h3>Unified Insights</h3><p>Lorem ipsum dolor sit amet consectetur.<br>Non malesuada euismod vestibulum urna cursus</p></div>
  <div class="benefit" style="left:342px;top:1013px"><div class="num">02</div><h3>Secure &amp; Compliant</h3><p>Lorem ipsum dolor sit amet consectetur.<br>Non malesuada euismod vestibulum urna cursus</p></div>
  <div class="benefit" style="left:618px;top:1013px"><div class="num">03</div><h3>Customizable Dashboards</h3><p>Lorem ipsum dolor sit amet consectetur.<br>Non malesuada euismod vestibulum urna cursus</p></div>
  <div class="benefit" style="left:891px;top:1013px"><div class="num">04</div><h3>Scalable &amp; Future-Proof</h3><p>Lorem ipsum dolor sit amet consectetur.<br>Non malesuada euismod vestibulum urna cursus</p></div>
</section>

<!-- about -->
<section>
  <h2 class="section-title display" style="left:60px;top:1275px">About Us</h2>
  <p class="abs body-copy" style="left:60px;top:1340px;width:610px">KORVEL is more than a platform — it's a mission. We help public and social sector organizations harness the power of data to serve communities better. From policy planning to frontline services, our tools enable informed action and measurable results.</p>
  <div class="stat-big" style="top:1492px"><strong>99%</strong><span>Clients<br>Satisfaction</span></div>
  <div class="abs" style="left:78px;top:1614px;width:101px;height:2px;background:#777"></div>
  <div class="stat-big" style="top:1644px"><strong>100%</strong><span>Work On<br>Field</span></div>
  <div class="btn" style="left:62px;top:1788px;width:208px;height:45px">See How It Works</div>
  <div class="abs" style="left:569px;top:1632px;width:215px;height:201px;border:6px solid var(--orange)"></div>
  <div class="placeholder" role="img" aria-label="Photo of a DNA helix and a hand holding a tablet" style="left:257px;top:1450px;width:416px;height:316px;background:linear-gradient(135deg,#0b2a45,#1f6c8e 55%,#c6dbe8)"></div>
  <div class="placeholder" role="img" aria-label="Photo of a hand pointing a pen at bar charts on a laptop" style="left:734px;top:1339px;width:406px;height:439px;background:linear-gradient(135deg,#c7c9cc,#3b4a6a 50%,#27334a)"></div>
</section>

<!-- platform -->
<section>
  <h2 class="section-title display" style="left:60px;top:1934px;line-height:35px">What our<br>platform do &amp;<br>why we best</h2>
  <p class="abs body-copy" style="left:60px;top:2094px;width:400px">Lorem ipsum dolor sit amet consectetur. Congue facilisis ante amet ullamcorper facilisis tempor quam pulvinar vestibulum. Urna blandit integer ultrices viverra aliquet risus egestas feugiat leo. Sollicitudin eget eget etiam adipiscing viverra posuere egestas.</p>
  <div class="btn" style="left:62px;top:2230px;width:167px;height:43px">Request a Demo</div>
  <div class="placeholder" role="img" aria-label="Photo of an analyst working at a desktop with data dashboards" style="left:561px;top:1911px;width:579px;height:387px;border-radius:10px;background:linear-gradient(135deg,#4a4038,#7c6f60 45%,#b8b2a8)"></div>
</section>

<!-- timeline -->
<section>
  <div class="abs" style="left:315px;top:2343px;width:134px;height:69px;background:var(--navy)"></div>
  <div class="abs" style="left:62px;top:2411px;width:1078px;height:2px;background:#6b6b6b"></div>
  <div class="step" style="left:88px">1</div>
  <div class="step" style="left:235px">2</div>
  <div class="step" style="left:382px;color:var(--white)">3</div>
  <div class="step" style="left:526px">4</div>
  <div class="step" style="left:671px">5</div>
  <div class="step" style="left:816px">6</div>
  <div class="step" style="left:961px">7</div>
  <div class="step" style="left:1107px">8</div>
  <div class="step-dot" style="left:88px"></div>
  <div class="step-dot" style="left:235px"></div>
  <div class="step-dot" style="left:382px;width:18px;height:18px;margin-left:-9px;top:2403px"></div>
  <div class="step-dot" style="left:526px"></div>
  <div class="step-dot" style="left:671px"></div>
  <div class="step-dot" style="left:816px"></div>
  <div class="step-dot" style="left:961px"></div>
  <div class="step-dot" style="left:1107px"></div>
  <p class="abs" style="left:302px;top:2431px;width:160px;text-align:center;font-size:14px;line-height:1.5">Lorem ipsum dolor sit amet</p>
</section>

<!-- smarter care -->
<section>
  <h2 class="section-title display" style="left:0;width:1200px;text-align:center;top:2556px;line-height:35px">Smarter care through<br>connected data</h2>
  <div class="acc-row" style="top:2679px"><span class="idx">01</span><span class="name">Electronic Health Record (EHR) integration</span><span class="icon"></span></div>
  <div class="acc-row" style="top:2754px"><span class="idx">02</span><span class="name">Predictive maintenance tools</span><span class="icon"></span></div>
  <div class="acc-row open" style="top:2829px;border-bottom:none"><span class="idx">03</span><span class="name">Outcome tracking &amp; analytics</span><span class="icon"></span></div>
  <div class="placeholder" role="img" aria-label="Photo of hands typing on a laptop showing an analytics dashboard" style="left:60px;top:2909px;width:1080px;height:417px;border-radius:14px;background:linear-gradient(110deg,#1e1710,#4a3b2c 40%,#c9c6c2 75%,#8a857f)"></div>
  <div class="metric-card">
    <div class="val" style="top:44px">412<small>hp</small></div>
    <p style="top:94px">Experience hassle-free car buying with our<br>extensive range of vehicles</p>
    <div class="val" style="top:172px">57<small>mph</small></div>
    <p style="top:222px">transparent team dedicatf satisfaction<br>Experience hassle-free</p>
  </div>
  <div class="btn" style="left:956px;top:3251px;width:136px;height:45px;border-radius:10px">Learn More</div>
</section>

<!-- testimonials -->
<section>
  <h2 class="section-title display" style="left:0;width:1200px;text-align:center;top:3408px">Testimonials</h2>
  <div class="avatar" role="img" aria-label="Portrait of Marcus T. Hale" style="left:564px;top:3481px;width:74px;height:74px"></div>
  <div class="avatar" role="img" aria-label="Client portrait" style="left:173px;top:3540px;width:54px;height:54px"></div>
  <div class="avatar" role="img" aria-label="Client portrait" style="left:152px;top:3640px;width:44px;height:44px"></div>
  <div class="avatar" role="img" aria-label="Client portrait" style="left:195px;top:3733px;width:28px;height:28px"></div>
  <div class="avatar" role="img" aria-label="Client portrait" style="left:974px;top:3540px;width:54px;height:54px"></div>
  <div class="avatar" role="img" aria-label="Client portrait" style="left:1006px;top:3640px;width:44px;height:44px"></div>
  <div class="avatar" role="img" aria-label="Client portrait" style="left:977px;top:3733px;width:28px;height:28px"></div>
  <p class="abs" style="left:0;width:1200px;text-align:center;top:3579px;font-size:22px">Marcus T. Hale</p>
  <p class="abs" style="left:0;width:1200px;text-align:center;top:3615px;font-size:16px;color:var(--muted)">Founder, Brightwater Care</p>
  <svg class="abs" style="left:540px;top:3660px" width="122" height="84" aria-hidden="true">
    <g fill="none" stroke="var(--orange)" stroke-width="7" stroke-linecap="round">
      <circle cx="28" cy="30" r="20"/><path d="M48 30C48 58 34 74 12 80"/>
      <circle cx="88" cy="30" r="20"/><path d="M108 30C108 58 94 74 72 80"/>
    </g>
  </svg>
  <p class="abs body-copy" style="left:290px;top:3770px;width:620px;text-align:center;line-height:1.7">Lorem ipsum dolor sit amet consectetur. In arcu mauris bibendum tortor dignissim purus. Nunc aliquam sagittis et velit dolor. Morbi scelerisque dolor rhoncus orci. Risus placerat.</p>
</section>

<!-- footer -->
<footer class="site-footer">
  <div class="abs" style="left:60px;top:72px;display:flex;align-items:center;gap:14px;font-size:50px;font-weight:700;color:var(--navy);letter-spacing:10px"><span style="width:18px;height:18px;background:var(--orange)"></span>KORVEL</div>
  <p class="abs body-copy" style="left:60px;top:188px;width:340px">Lorem ipsum dolor sit amet consectetur. Imperdiet et molestie duis condimentum est.</p>
  <div class="foot-col">
    <h4 style="left:544px;top:64px">Use Full Links</h4>
    <span class="foot-link" style="left:544px;top:117px">Home</span>
    <span class="foot-link" style="left:544px;top:154px">About Us</span>
    <span class="foot-link" style="left:544px;top:193px">Platform</span>
    <span class="foot-link" style="left:544px;top:228px">Solutions</span>
    <span class="foot-link" style="left:544px;top:265px">Resources</span>
  </div>
  <div class="foot-divider" style="left:744px"></div>
  <div class="foot-col">
    <h4 style="left:813px;top:64px">Follow Us</h4>
    <span class="foot-link" style="left:813px;top:113px"><span class="foot-dot"></span>Circlebook</span>
    <span class="foot-link" style="left:813px;top:155px"><span class="foot-dot"></span>Pictoria</span>
    <span class="foot-link" style="left:813px;top:196px"><span class="foot-dot"></span>Workweb</span>
    <span class="foot-link" style="left:813px;top:237px"><span class="foot-dot"></span>Portfolia</span>
  </div>
  <div class="foot-divider" style="left:981px"></div>
  <div class="foot-col">
    <h4 style="left:1048px;top:64px">Legal</h4>
    <span class="foot-link" style="left:1048px;top:117px">Terms Of Use</span>
    <span class="foot-link" style="left:1048px;top:154px">Privacy Policy</span>
    <span class="foot-link" style="left:1048px;top:192px">Cookie Policy</span>
  </div>
  <div class="abs" style="left:80px;top:355px;width:1040px;height:1px;background:#d5d5d5"></div>
  <p class="abs" style="left:0;width:1200px;text-align:center;top:369px;font-size:12px">Copyright © 2025 All Rights Reserved.</p>
</footer>

</body>
</html>
```